Business card for utility of the future

I need a business card template designed for brookvane. We provide sustainable water, energy and waste services to homes.

The card should include name, position, email address, phone number, website and our logo (attached). I would like it to convey professionalism and creativity.

Target Market(s)

Homeowners, investors, corporate partners.

Industry/Entity Type

Utility

Contact Information for Business Card

The card should include name, position, email address, phone number, website and our logo (attached).

```html
<!DOCTYPE html>
<html lang="en">
<head>
<meta charset="utf-8">
<title>brookvane business card</title>
<link href="https://fonts.googleapis.com/css2?family=Questrial&display=swap" rel="stylesheet">
<style>
  :root {
    --backdrop: #ece9e4;
    --card: #ffffff;
    --green: #6cc58e;
    --ink: #4a4a4a;
    --ink-light: #6b6b6b;
    --ink-faint: #b5b5b5;
  }
  * { margin: 0; padding: 0; box-sizing: border-box; }
  html, body {
    width: 1200px;
    height: 1200px;
    overflow: hidden;
    background: var(--backdrop);
    font-family: "Questrial", "Century Gothic", sans-serif;
  }
  .sheet {
    width: 1200px;
    height: 1200px;
    display: flex;
    flex-direction: column;
    align-items: center;
    justify-content: center;
    gap: 60px;
  }
  .card {
    position: relative;
    width: 840px;
    height: 480px;
    background: var(--card);
    box-shadow: 0 4px 14px rgba(0,0,0,0.10);
  }

  /* Front */
  .card-front .brand {
    position: absolute;
    left: 40px;
    top: 0;
    width: 380px;
    height: 480px;
    display: flex;
    align-items: center;
    justify-content: center;
  }
  .brand-name {
    font-size: 64px;
    color: var(--ink);
    line-height: 1;
    white-space: nowrap;
  }
  .divider {
    position: absolute;
    left: 450px;
    top: 70px;
    width: 2px;
    height: 340px;
    background: var(--green);
  }
  .details {
    position: absolute;
    left: 490px;
    top: 80px;
    right: 30px;
  }
  .person-name {
    font-size: 30px;
    color: var(--ink);
    line-height: 1.1;
  }
  .person-role {
    font-size: 17px;
    color: var(--green);
    margin-top: 4px;
  }
  .contact-list {
    list-style: none;
    margin-top: 70px;
  }
  .contact-item {
    display: flex;
    align-items: center;
    gap: 12px;
    font-size: 19px;
    color: var(--ink-light);
    margin-bottom: 12px;
    white-space: nowrap;
  }
  .contact-icon {
    width: 20px;
    height: 20px;
    flex: none;
  }

  /* Back */
  .card-back {
    display: flex;
    align-items: center;
    justify-content: center;
  }
  .card-back .brand-name {
    font-size: 92px;
    color: var(--ink-faint);
  }
</style>
</head>
<body>
<main class="sheet">
  <section class="card card-front" aria-label="Card front">
    <div class="brand">
      <span class="brand-name">brookvane</span>
    </div>
    <div class="divider"></div>
    <div class="details">
      <p class="person-name">Daniel Marsh</p>
      <p class="person-role">Owner</p>
      <ul class="contact-list">
        <li class="contact-item">
          <svg class="contact-icon" viewBox="0 0 20 20" aria-hidden="true">
            <rect width="20" height="20" rx="2" fill="#6cc58e"/>
            <path d="M6 4.5 L8.2 4.5 L9 7.5 L7.6 8.6 Q8.8 11.2 11.4 12.4 L12.5 11 L15.5 11.8 L15.5 14 Q15.5 15.5 14 15.5 Q4.5 15 4.5 6 Q4.5 4.5 6 4.5 Z" fill="#fff"/>
          </svg>
          (415) 555-0182
        </li>
        <li class="contact-item">
          <svg class="contact-icon" viewBox="0 0 20 20" aria-hidden="true">
            <rect width="20" height="20" rx="2" fill="#6cc58e"/>
            <rect x="4" y="6" width="12" height="8" fill="none" stroke="#fff" stroke-width="1.4"/>
            <path d="M4 6 L10 11 L16 6" fill="none" stroke="#fff" stroke-width="1.4"/>
          </svg>
          info@brookvane.com
        </li>
        <li class="contact-item">
          <svg class="contact-icon" viewBox="0 0 20 20" aria-hidden="true">
            <rect width="20" height="20" rx="2" fill="#6cc58e"/>
            <circle cx="10" cy="10" r="5.5" fill="none" stroke="#fff" stroke-width="1.3"/>
            <ellipse cx="10" cy="10" rx="2.3" ry="5.5" fill="none" stroke="#fff" stroke-width="1.1"/>
            <line x1="4.5" y1="10" x2="15.5" y2="10" stroke="#fff" stroke-width="1.1"/>
          </svg>
          www.brookvane.com
        </li>
        <li class="contact-item">
          <svg class="contact-icon" viewBox="0 0 20 20" aria-hidden="true">
            <rect width="20" height="20" rx="2" fill="#6cc58e"/>
            <path d="M10 16 Q5 10.5 5 8 A5 5 0 0 1 15 8 Q15 10.5 10 16 Z" fill="#fff"/>
            <circle cx="10" cy="8" r="1.8" fill="#6cc58e"/>
          </svg>
          48 Harbour Lane, Millbrook.
        </li>
      </ul>
    </div>
  </section>

  <section class="card card-back" aria-label="Card back">
    <span class="brand-name">brookvane</span>
  </section>
</main>
</body>
</html>
```